Business Card Design for company

We want new business cards. We'd like something different-- yet still highly professional. Our tagline is Providing leadership, delivering success. Stock photos are ok, as long as they are relevant and look upscale.

Target Market(s)

Architecture/Business Management Consulting/Engineering Consulting

Contact Information for Business Card

dark gray background with pops of blue might be good, but you tell me. You're the designers. Rounded corners might be nice, but again, you tell me.

Font styles to use
Serif
Sans Serif

Colors
3276b5
5c5c5c
9d9d9d
fbfbfb

Requirements
Nice to have
• Something different, but still very professional.

```html
<!DOCTYPE html>
<html lang="en">
<head>
<meta charset="UTF-8">
<title>Norvale Group – Business Cards</title>
<link href="https://fonts.googleapis.com/css2?family=Montserrat:wght@600&family=Work+Sans:wght@400;500&display=swap" rel="stylesheet">
<style>
  :root {
    --brand-blue: #2a6498;
    --accent-blue: #3276b5;
    --ink-gray: #5c5c5c;
    --rule-gray: #9d9d9d;
    --paper: #fbfbfb;
    --backdrop: #d9d9d9;
  }
  * { margin: 0; padding: 0; box-sizing: border-box; }
  html, body { width: 1200px; height: 930px; overflow: hidden; }
  body {
    background: var(--backdrop);
    font-family: "Work Sans", Arial, sans-serif;
    position: relative;
  }
  .card {
    position: absolute;
    width: 560px;
    height: 320px;
    box-shadow: 0 6px 18px rgba(0,0,0,0.25);
  }

  /* Back of card */
  .card-back {
    left: 60px;
    top: 100px;
    background: var(--brand-blue);
    color: #fff;
    display: flex;
    flex-direction: column;
    align-items: center;
    justify-content: center;
  }
  .card-back .wordmark {
    font-family: "Montserrat", Arial, sans-serif;
    font-weight: 600;
    font-size: 44px;
    letter-spacing: 3px;
    color: #fff;
    text-align: center;
    line-height: 1.15;
  }
  .card-back .web-strip {
    display: flex;
    align-items: center;
    gap: 12px;
    margin-top: 48px;
    font-size: 13px;
    letter-spacing: 0.5px;
  }
  .card-back .web-strip .rule {
    width: 110px;
    height: 1px;
    background: rgba(255,255,255,0.7);
  }

  /* Front of card */
  .card-front {
    left: 580px;
    top: 500px;
    background: #fff;
  }
  .card-front .wordmark {
    position: absolute;
    right: 40px;
    top: 36px;
    font-family: "Montserrat", Arial, sans-serif;
    font-weight: 600;
    font-size: 36px;
    letter-spacing: 2px;
    line-height: 1.1;
    color: var(--accent-blue);
    text-align: right;
  }
  .card-front .divider {
    position: absolute;
    left: 40px;
    right: 0;
    top: 160px;
    height: 1px;
    background: var(--ink-gray);
  }
  .card-front .person {
    position: absolute;
    left: 40px;
    top: 128px;
  }
  .card-front .person-name {
    font-size: 24px;
    font-weight: 500;
    color: var(--accent-blue);
    letter-spacing: 1px;
    text-transform: uppercase;
  }
  .card-front .person-role {
    margin-top: 8px;
    font-size: 14px;
    color: var(--ink-gray);
  }
  .card-front .contact {
    position: absolute;
    right: 40px;
    top: 176px;
    width: 230px;
    font-size: 13px;
    color: var(--ink-gray);
    line-height: 1.4;
  }
  .card-front .address { margin-bottom: 18px; }
  .card-front .contact-line {
    display: flex;
    align-items: center;
    gap: 8px;
  }
  .card-front .contact-line svg { width: 11px; height: 11px; flex: none; }
  .card-front .contact-line .hl { color: var(--accent-blue); }
</style>
</head>
<body>
  <section class="card card-back" aria-label="Business card back">
    <div class="wordmark">NORVALE<br>GROUP</div>
    <div class="web-strip">
      <span class="rule"></span>
      <span>www.norvalegroup.com</span>
      <span class="rule"></span>
    </div>
  </section>

  <section class="card card-front" aria-label="Business card front">
    <div class="wordmark">NORVALE<br>GROUP</div>
    <div class="divider"></div>
    <div class="person">
      <div class="person-name">Daniel Hartley</div>
    </div>
    <div class="person" style="top:166px">
      <div class="person-role">Director</div>
    </div>
    <div class="contact">
      <div class="address">212 Harbour Lane,<br>Riverton, NZ, 7042</div>
      <div class="contact-line">
        <svg viewBox="0 0 12 12"><path d="M3 1 L5 3 L4 4.5 Q5 7 7.5 8 L9 7 L11 9 L9.5 11 Q2 10 1 2.5 Z" fill="var(--accent-blue)"/></svg>
        <span>(555) 014-2291</span>
      </div>
      <div class="contact-line">
        <svg viewBox="0 0 12 12"><rect x="1" y="2.5" width="10" height="7" fill="none" stroke="var(--accent-blue)" stroke-width="1.2"/><path d="M1 2.5 L6 6.5 L11 2.5" fill="none" stroke="var(--accent-blue)" stroke-width="1.2"/></svg>
        <span>info@norvalegroup.com</span>
      </div>
      <div class="contact-line">
        <svg viewBox="0 0 12 12"><circle cx="6" cy="6" r="5" fill="none" stroke="var(--accent-blue)" stroke-width="1.1"/><ellipse cx="6" cy="6" rx="2.2" ry="5" fill="none" stroke="var(--accent-blue)" stroke-width="1"/><line x1="1" y1="6" x2="11" y2="6" stroke="var(--accent-blue)" stroke-width="1"/></svg>
        <span>www.<span class="hl">norvalegroup</span>.com</span>
      </div>
    </div>
  </section>
</body>
</html>
```